The Brightwater Compass Business Card

We need an attractive business card with the logo that we bought from ArtVantly last year.
Our mission is to contribute to change the way today's leaders manage business companies bringing value to the workplace and helping them to build a new model of creating wealth.
Our logo is clear about our values : we seek Positive Change through People and are convinced that the pursuit of individual well-being and the chase of economic results can converge with the right management.
Management Consulting
Corinne Fabrelle
+34 612 98 70 31
corinne.fabrelle@thebrightwatercompass-mail.net
www.thebrightwatercompass-mail.net

```html
<!DOCTYPE html>
<html lang="en">
<head>
<meta charset="utf-8">
<title>The Brightwater Compass — Business Card</title>
<link rel="stylesheet" href="https://fonts.googleapis.com/css2?family=Cinzel:wght@400;500&family=Roboto+Condensed:wght@400&display=swap">
<style>
  :root {
    --canvas: #ecedee;
    --teal: #0f9a82;
    --teal-bright: #05a58a;
    --teal-deep: #0a5a4b;
    --teal-night: #06382f;
    --card-white: #f6f6f6;
    --card-grey: #e2e3e4;
    --silver: #c9d2cf;
    --mark-faint: #d9dedd;
  }
  * { box-sizing: border-box; margin: 0; padding: 0; }
  html, body { width: 1200px; height: 900px; overflow: hidden; }
  body {
    background: var(--canvas);
    display: flex;
    align-items: center;
    justify-content: center;
    gap: 70px;
  }
  .card {
    position: relative;
    width: 400px;
    height: 700px;
    overflow: hidden;
    box-shadow: 0 6px 18px rgba(0,0,0,0.12);
  }

  /* Shared brand lockup: mark above name, centred */
  .brand {
    display: flex;
    flex-direction: column;
    align-items: center;
    gap: 14px;
    font-family: "Cinzel", serif;
    font-weight: 400;
    white-space: nowrap;
    text-align: center;
  }
  .brand__dot {
    width: 46px; height: 46px;
    border-radius: 50%;
    background: currentColor;
    flex: none;
  }

  /* Back of card */
  .card--back {
    background: radial-gradient(circle at 50% 45%, #13987f 0%, var(--teal-deep) 55%, var(--teal-night) 100%);
    display: flex;
    flex-direction: column;
    align-items: center;
    justify-content: center;
    gap: 16px;
    color: var(--silver);
  }
  .card--back .brand { font-size: 24px; }
  .card--back .website {
    font-family: "Roboto Condensed", sans-serif;
    font-size: 14px;
    color: var(--silver);
  }

  /* Front of card */
  .card--front {
    background: radial-gradient(circle at 45% 40%, var(--card-white) 0%, var(--card-grey) 100%);
    border-left: 5px solid var(--teal);
  }
  .card--front .brand {
    position: absolute;
    top: 56px; left: 0; right: 0;
    font-size: 21px;
    color: var(--teal-deep);
  }
  .tree-motif {
    position: absolute;
    left: 150px; top: 260px;
    width: 330px; height: 330px;
  }
  .contact {
    position: absolute;
    top: 250px; left: 30px; right: 20px;
    font-family: "Roboto Condensed", sans-serif;
    color: var(--teal);
  }
  .contact__name {
    font-family: "Cinzel", serif;
    font-weight: 500;
    font-size: 30px;
    letter-spacing: 0.5px;
    margin-bottom: 10px;
    white-space: nowrap;
  }
  .contact__line { font-size: 16px; line-height: 1.5; white-space: nowrap; }
  .wave {
    position: absolute;
    left: 0; bottom: 0;
    width: 400px; height: 320px;
  }
  .card--front .website {
    position: absolute;
    right: 26px; bottom: 28px;
    font-family: "Roboto Condensed", sans-serif;
    font-size: 16px;
    color: #ffffff;
  }
</style>
</head>
<body>
  <section class="card card--back" aria-label="Card back">
    <div class="brand"><span class="brand__dot"></span>The Brightwater Compass</div>
    <p class="website">www.thebrightwatercompass-mail.net</p>
  </section>

  <section class="card card--front" aria-label="Card front">
    <div class="brand"><span class="brand__dot"></span>The Brightwater Compass</div>

    <svg class="tree-motif" viewBox="0 0 330 330" role="img" aria-label="Faint decorative tree of people motif">
      <defs>
        <radialGradient id="motifFade" cx="50%" cy="50%" r="50%">
          <stop offset="0%" stop-color="#d9dedd" stop-opacity="0.9"/>
          <stop offset="100%" stop-color="#d9dedd" stop-opacity="0"/>
        </radialGradient>
      </defs>
      <circle cx="165" cy="165" r="165" fill="url(#motifFade)"/>
    </svg>

    <div class="contact">
      <h1 class="contact__name">Corinne Fabrelle</h1>
      <p class="contact__line">+34 612 98 70 31</p>
      <p class="contact__line">corinne.fabrelle@thebrightwatercompass-mail.net</p>
    </div>

    <svg class="wave" viewBox="0 0 400 320" aria-hidden="true">
      <path d="M0 250 C 140 240, 260 160, 400 0 L 400 320 L 0 320 Z" fill="#8fd3c5"/>
      <path d="M0 268 C 150 255, 270 175, 400 24 L 400 320 L 0 320 Z" fill="#05a58a"/>
    </svg>
    <p class="website">www.thebrightwatercompass-mail.net</p>
  </section>
</body>
</html>
```